Dryer Vent Cleaning Postcard Design

We need a postcard design for Flue Wranglers, a company that specializes in dryer vent cleaning, repairs and upgrades. Dryer vents need periodic cleaning to avoid lint clogging, dryer malfunction, long dry times and even a house fire. This card will be sent to residential and businesses prospects to introduce them to our services and the importance of maintaining their dryer vents. Our website is @ fluewrangling.com and provides information about our services, photos of our work and our general color scheme (purple/orange). Final print size will be 5x7 horizontal.

Target Market(s)

homeowners and business owners (spas, salons, grooming, gyms, laundrymats, etc)

Requirements
Must have
• Reduce the risk of fire
shortened dry times
lower energy consumption
18000 dryer fires caused in the US per year
Nice to have
• Does your dryer take too long to dry?

```html
<!DOCTYPE html>
<html lang="en">
<head>
<meta charset="utf-8">
<title>Flue Wranglers – Dryer Vent Cleaning Postcard</title>
<link rel="stylesheet" href="https://fonts.googleapis.com/css2?family=Alfa+Slab+One&family=Roboto+Slab:wght@700;800&family=Oswald:wght@600&display=swap">
<style>
  :root {
    --purple: #3f3370;
    --orange: #ec7545;
    --white: #ffffff;
    --paper: #f6f6f8;
    --backdrop: #e4e4e6;
    --tan: #c9b596;
    --steel: #bfbcc0;
    --sky: #7b9fd6;
  }
  * { margin: 0; padding: 0; box-sizing: border-box; }
  html, body { width: 1200px; height: 516px; overflow: hidden; background: var(--backdrop); }
  .canvas { position: relative; width: 1200px; height: 516px; }

  .card {
    position: absolute; top: 74px; width: 515px; height: 368px;
    background: linear-gradient(120deg, var(--white) 0%, var(--paper) 60%, var(--white) 100%);
    overflow: hidden; box-shadow: 0 2px 6px rgba(0,0,0,.18);
    font-family: "Roboto Slab", Georgia, serif; font-weight: 800;
  }
  .card--front { left: 74px; }
  .card--back { left: 610px; }

  .art { position: absolute; }

  /* Front */
  .headline-lead { position: absolute; left: 31px; top: 28px; font-size: 25px; color: var(--purple); font-weight: 800; letter-spacing: .3px; }
  .headline-fire { position: absolute; left: 28px; top: 50px; font-family: "Alfa Slab One", Georgia, serif; font-weight: 400; font-size: 96px; line-height: 1; color: var(--orange); letter-spacing: 2px; }
  .headline-sub { position: absolute; left: 31px; top: 144px; font-size: 18.5px; color: var(--purple); letter-spacing: .2px; }

  .brand { position: absolute; left: 318px; top: 128px; width: 180px; display: flex; align-items: center; gap: 6px; justify-content: center; }
  .brand-dot { width: 14px; height: 14px; border-radius: 50%; background: var(--orange); flex: none; }
  .brand-name { font-size: 19px; color: var(--purple); white-space: nowrap; }

  .front-rule { position: absolute; left: 0; top: 183px; width: 100%; height: 3px; background: var(--purple); }
  .front-band { position: absolute; left: 0; top: 186px; width: 100%; height: 96px; background: var(--orange); }

  .front-panel { position: absolute; left: 226px; top: 281px; width: 289px; height: 87px; background: var(--purple); clip-path: polygon(10% 0, 100% 0, 100% 100%, 0 100%); }
  .energy { position: absolute; right: 11px; top: 292px; font-size: 14.5px; color: var(--white); letter-spacing: .3px; }
  .fact { position: absolute; right: 11px; top: 310px; font-size: 9.6px; color: var(--white); letter-spacing: .3px; }
  .call-strip { position: absolute; left: 242px; top: 323px; width: 273px; height: 30px; background: var(--orange); clip-path: polygon(4% 0, 100% 0, 100% 100%, 0 100%); }
  .call-strip-text { position: absolute; right: 11px; top: 327px; font-size: 16px; color: var(--white); letter-spacing: .3px; }

  .bubble { position: absolute; border-radius: 50%; border: 3px solid var(--orange); }

  /* Back */
  .back-stripe { position: absolute; inset: 0; background: var(--orange); clip-path: polygon(0 0, 264px 0, 336px 100%, 0 100%); }
  .back-panel { position: absolute; inset: 0; background: var(--purple); clip-path: polygon(0 0, 258px 0, 328px 100%, 0 100%); }
  .services-band { position: absolute; left: 0; top: 156px; width: 100%; height: 118px; background: var(--orange); clip-path: polygon(0 0, 284px 0, 302px 100%, 0 100%); }
  .services-title { position: absolute; left: 30px; top: 168px; font-size: 15.5px; color: var(--white); letter-spacing: .2px; }
  .services-list { position: absolute; left: 30px; top: 191px; list-style: none; color: var(--white); font-size: 11.6px; line-height: 14.7px; }
  .services-list li::before { content: ""; display: inline-block; width: 7px; height: 7px; border-radius: 50%; background: var(--white); margin-right: 5px; vertical-align: 1px; }

  .back-call { position: absolute; left: 0; width: 310px; text-align: center; top: 282px; font-size: 16.5px; color: var(--white); }
  .back-phone { position: absolute; left: 0; width: 310px; text-align: center; top: 298px; font-family: "Oswald", Arial, sans-serif; font-weight: 600; font-size: 33px; line-height: 1.2; color: var(--orange); letter-spacing: .5px; }
  .back-web { position: absolute; left: 29px; top: 337px; font-size: 16.5px; color: var(--white); letter-spacing: .2px; }
</style>
</head>
<body>
<main class="canvas">

  <section class="card card--front" aria-label="Postcard front">
    <h1>
      <span class="headline-lead">Reduce the risk of</span>
      <span class="headline-fire">FIRE</span>
      <span class="headline-sub">SHORTENED DRY TIMES</span>
    </h1>

    <div class="art" role="img" aria-label="Mascot technician with vacuum and brush in a round badge" style="left:344px;top:18px;width:120px;height:110px;border-radius:50% 50% 10% 10%;background:radial-gradient(circle at 50% 60%, var(--sky), #5d7fc0 70%, var(--orange) 72%);"></div>
    <div class="brand">
      <span class="brand-dot"></span>
      <span class="brand-name">Flue Wranglers</span>
    </div>

    <div class="front-rule"></div>
    <div class="front-band"></div>
    <div class="art" role="img" aria-label="Technician holding a vent brush beside a wall vent, flexible duct and front-load dryer" style="left:10px;top:186px;width:495px;height:96px;background:linear-gradient(90deg, rgba(201,181,150,.75) 0%, rgba(201,181,150,.55) 30%, rgba(191,188,192,.7) 60%, rgba(225,222,224,.85) 100%);"></div>

    <div class="bubble art" role="img" aria-label="Top-load dryer with lint bursting out" style="left:35px;top:280px;width:92px;height:88px;background:linear-gradient(160deg, var(--steel), #e8e6e8);"></div>
    <div class="bubble art" role="img" aria-label="Technician resting a vent brush on his shoulder" style="left:136px;top:280px;width:92px;height:88px;background:radial-gradient(circle, var(--tan) 30%, var(--purple) 60%);"></div>

    <div class="front-panel"></div>
    <p class="energy">LOWER ENERGY CONSUMPTION</p>
    <p class="fact">18000 dryer fires caused in the US per year</p>
    <div class="call-strip"></div>
    <p class="call-strip-text">Call Today! 555-014-2297</p>
  </section>

  <section class="card card--back" aria-label="Postcard back">
    <div class="back-stripe"></div>
    <div class="back-panel"></div>

    <div class="art" role="img" aria-label="Technician with a red vent vacuum next to a dryer overflowing with lint" style="left:30px;top:10px;width:230px;height:146px;background:linear-gradient(90deg, rgba(201,181,150,.45), rgba(210,50,50,.45) 40%, rgba(230,228,230,.55) 70%);"></div>

    <div class="services-band"></div>
    <h2 class="services-title">SERVICES WE PROVIDED</h2>
    <ul class="services-list">
      <li>Dryer Vent Cleaning</li>
      <li>Dryer Vent Repair &amp; Installation</li>
      <li>Transition Vent Replacement</li>
      <li>Vent Cap Replacement</li>
      <li>Bird / Rodent Guard</li>
    </ul>

    <div class="bubble art" role="img" aria-label="Technician resting a vent brush on his shoulder" style="left:244px;top:172px;width:118px;height:122px;background:radial-gradient(circle, var(--tan) 28%, var(--purple) 58%);"></div>

    <p class="back-call">CALL TODAY!</p>
    <p class="back-phone">555-014-2297</p>
    <p class="back-web">fluewrangling.com</p>
  </section>

</main>
</body>
</html>
```